Tutoring Site Hero Image Design

Updated Hero Concept for BrightlaneLessons.com

Create a hero that communicates “high quality, in-person private tutoring for all ages,” with warmth, credibility, and a real-life feel. The hero should move away from generic stock photography and better reflect the moments that make our service different: tutors meeting students where they are, one-on-one engagement, and a range of ages.

What the New Hero Should Convey
1. In-person, private, one-on-one support
This is the core differentiator, so the visual should feel intimate, focused, and real. Avoid anything that resembles online learning settings or learning-center classrooms.

2. Coverage of age ranges without clutter
We serve elementary through college. We do not need multiple students in the hero, but the chosen student should not skew strongly to one age group. Aim for a middle-ground age that feels inclusive, for example a middle schooler or early high schooler.

3. Realistic, authentic moments
Use photography that feels candid and warm. Natural light, home settings, kitchen tables, quiet study nooks, or library corners work well. Avoid staged stock looks, harsh lighting, or exaggerated classroom setups.

Design the hero at 2400 × 1200 px, with the focal point on the right side, safe area leaving room on the left for a stacked headline and form.

Images that I've shared as just thought starters and do not need to be used in the design.

Font styles to use
Sans Serif

Colors
0054AA
0677BA
7BADD7
CADEEF
E8F1F8
EB3D1F
EC4F4E
F09395
F8D3D4
FCEDEE
6B429C
8869AF
B7A5CE
E3DAEB
F3F0F8

```html
<!DOCTYPE html>
<html lang="en">
<head>
<meta charset="utf-8">
<title>Brightlane Lessons – Hero</title>
<link rel="stylesheet" href="https://fonts.googleapis.com/css2?family=Lato:wght@400;700;900&display=swap">
<style>
  :root {
    --stage: #4a4a4a;
    --ink: #1d1d1f;
    --red: #e4002b;
    --navy: #232f6e;
    --blush: #f8d3d4;
    --blush-soft: #fcedee;
    --sky: #dcebf8;
    --sky-deep: #c3d3ea;
    --photo-warm: #b9a392;
    --photo-cool: #8d9bb0;
  }
  * { box-sizing: border-box; margin: 0; padding: 0; }
  html, body {
    width: 1200px; height: 899px; overflow: hidden;
    background: var(--stage);
    font-family: "Lato", sans-serif;
  }
  .hero {
    position: absolute; left: 20px; top: 160px;
    width: 1160px; height: 580px; overflow: hidden;
    background:
      radial-gradient(ellipse 520px 380px at 5% 95%, rgba(240,147,149,0.55), transparent 70%),
      radial-gradient(ellipse 600px 420px at 80% 95%, var(--sky-deep), transparent 70%),
      linear-gradient(100deg, var(--blush) 0%, var(--blush-soft) 40%, #e9e6f1 65%, var(--sky) 100%);
  }
  .headline {
    position: absolute; left: 103px; top: 118px;
    font-weight: 900; font-size: 61px; line-height: 61px;
    letter-spacing: -1.5px; color: var(--ink);
  }
  .headline .accent { color: var(--red); }
  .intro {
    position: absolute; left: 103px; top: 317px; width: 485px;
    font-size: 14.6px; line-height: 19.4px; color: #2a2a2c;
  }
  .actions {
    position: absolute; left: 98px; top: 433px;
    display: flex; gap: 14px;
  }
  .btn {
    height: 36px; border-radius: 18px;
    display: flex; align-items: center; justify-content: center;
    font-size: 22px; font-weight: 700; letter-spacing: -0.3px;
  }
  .btn-quote { width: 160px; border: 1.5px solid var(--ink); color: var(--ink); }
  .btn-call { width: 248px; background: var(--red); color: #fff; }
  .tile { position: absolute; border-radius: 12px; }
  .tile-red { left: 605px; top: 97px; width: 215px; height: 82px; background: var(--red); }
  .tile-photo-tutor {
    left: 605px; top: 195px; width: 215px; height: 289px;
    background: linear-gradient(160deg, #c9cdd3 0%, var(--photo-cool) 45%, #7f8ea6 100%);
  }
  .tile-photo-study {
    left: 836px; top: 97px; width: 215px; height: 243px;
    background: linear-gradient(150deg, #d8c7b0 0%, var(--photo-warm) 55%, #c9a57a 100%);
  }
  .tile-navy { left: 836px; top: 357px; width: 135px; height: 127px; background: var(--navy); }
</style>
</head>
<body>
  <section class="hero">
    <h1 class="headline">
      Local Tutors.<br>
      <span class="accent">1-on-1</span> Learning.<br>
      Real Results.
    </h1>
    <p class="intro">For over 20 years, Brightlane Lessons has introduced students and families in our communities to experienced, professional, independent tutors who offer individualized, student-centered support across all grades and subjects, from kindergarten through college.</p>
    <div class="actions">
      <span class="btn btn-quote">Get a Quote</span>
      <span class="btn btn-call">Call (888) 555-0142</span>
    </div>
    <div class="tile tile-red"></div>
    <div class="tile tile-photo-tutor" role="img" aria-label="Photo of a tutor helping a young boy with his work at a table"></div>
    <div class="tile tile-photo-study" role="img" aria-label="Photo of a smiling student writing in a notebook beside her tutor"></div>
    <div class="tile tile-navy" role="img" aria-label="Navy tile with a faint book decoration"></div>
  </section>
</body>
</html>
```